Stationary for Corwin Lattimore | ||
Business card, letterhead, with compliments slip, envelope | ||
Use same font as used in my logo | ||
Corporate Traditional Professional Simple |
[firstname] [surname] | ||
[title] | ||
1 Some Street Sometown Somewhereshire SW23 8SW |
someone@corwinlattimore.example | ||
www.corwinlattimore.example | ||
I am the sole employee at the moment. In the future, I hope to have other employees, so I will add a 'title' section later. Please bear this in mind when positioning the information. I am looking for something that is elegant, professional, minimilistic and tasteful. Please take a look at the website: http://www.corwinlattimore.example using the following credentials to log in: u/n: "pinewhisk" p/w: "pinewhisk847" Please feel free to message me for more information. Most importantly, I want the logo and other key information (like my name?) to be in silver (PMS 877 Metallic). |
I am flexible on this. I want space on my business cards for people to be able to write some information on. | ||

```html
<!DOCTYPE html>
<html lang="en">
<head>
<meta charset="utf-8">
<title>Corwin Lattimore — Stationery</title>
<link rel="stylesheet" href="https://fonts.googleapis.com/css2?family=Cormorant+Garamond:wght@400&family=Lato:wght@400&display=swap">
<style>
  :root {
    --backdrop: #d6d6d6;
    --paper: #ffffff;
    --band: #666666;
    --band-dark: #555555;
    --silver: #9a9a9a;
    --silver-light: #dcdcdc;
    --ink: #6e6e6e;
    --ink-light: #eeeeee;
    --rule: #bdbdbd;
  }
  * { margin: 0; padding: 0; box-sizing: border-box; }
  html, body { width: 1200px; height: 1088px; overflow: hidden; }
  body {
    background: var(--backdrop);
    position: relative;
    font-family: "Lato", Arial, sans-serif;
    color: var(--ink);
  }
  .sheet { position: absolute; background: var(--paper); box-shadow: 0 2px 6px rgba(0,0,0,.18); overflow: hidden; }

  .wordmark {
    position: absolute;
    font-family: "Cormorant Garamond", "Times New Roman", serif;
    font-weight: 400;
    letter-spacing: .02em;
    line-height: 1;
    white-space: nowrap;
  }

  .contact {
    position: absolute;
    font-style: normal;
    font-size: 7px;
    line-height: 1.5;
    letter-spacing: .02em;
    white-space: nowrap;
  }

  /* Letterhead */
  .letterhead { left: 60px; top: 148px; width: 560px; height: 792px; }
  .letterhead .header-band { position: absolute; left: 0; top: 0; width: 100%; height: 92px; background: var(--band); }
  .letterhead .wordmark { left: 34px; top: 34px; font-size: 24px; color: var(--silver-light); }
  .letterhead .contact { right: 40px; top: 26px; color: var(--ink-light); }
  .letterhead .footer-band {
    position: absolute; left: 0; bottom: 0; width: 100%; height: 22px; background: var(--band);
    color: var(--ink-light); font-size: 6.5px; letter-spacing: .12em; text-transform: uppercase;
    display: flex; align-items: center; justify-content: center;
  }

  /* Envelope */
  .envelope { left: 680px; top: 148px; width: 460px; height: 230px; }
  .envelope .flap-band { position: absolute; left: 0; top: 0; width: 100%; height: 46px; background: var(--band); }
  .envelope .flap-wordmark { right: 40px; top: 16px; font-size: 14px; color: var(--silver-light); transform: rotate(180deg); }
  .envelope .body-wordmark { left: 24px; top: 70px; font-size: 20px; color: var(--silver); }
  .envelope .contact { left: 24px; bottom: 20px; }

  /* Business cards */
  .card { width: 320px; height: 183px; }
  .card-front { left: 680px; top: 430px; }
  .card-front .write-lines { position: absolute; left: 22px; top: 26px; width: 130px; }
  .card-front .write-lines span { display: block; height: 16px; border-bottom: 1px solid var(--rule); }
  .card-front .wordmark { left: 168px; top: 30px; font-size: 16px; color: var(--silver); }
  .card-front .contact { left: 168px; top: 94px; }
  .card-front .contact .person { font-size: 8px; color: var(--silver); }

  .card-back { left: 820px; top: 660px; background: var(--band-dark); }
  .card-back .wordmark { left: 40px; top: 42px; font-size: 22px; color: var(--silver-light); }
  .card-back .web {
    position: absolute; left: 0; bottom: 22px; width: 100%; text-align: center;
    color: #e6e6e6; font-size: 7px; letter-spacing: .14em; text-transform: uppercase;
  }
  .card-back .web::before {
    content: ""; display: block; width: 240px; height: 1px; background: #8a8a8a; margin: 0 auto 8px;
  }
</style>
</head>
<body>

  <section class="sheet letterhead" aria-label="Letterhead">
    <div class="header-band">
      <div class="wordmark">Corwin Lattimore</div>
      <address class="contact">
        1 Some Street, Sometown<br>
        Somewhereshire SW23 8SW<br>
        Phone: +44 (0)1632 960 412<br>
        Fax: +44 (0)1632 960 413<br>
        someone@corwinlattimore.example
      </address>
    </div>
    <div class="footer-band">www.corwinlattimore.example</div>
  </section>

  <section class="sheet envelope" aria-label="Envelope">
    <div class="flap-band">
      <div class="wordmark flap-wordmark">Corwin Lattimore</div>
    </div>
    <div class="wordmark body-wordmark">Corwin Lattimore</div>
    <address class="contact">
      1 Some Street, Sometown<br>
      Somewhereshire SW23 8SW<br>
      Phone: +44 (0)1632 960 412<br>
      Fax: +44 (0)1632 960 413<br>
      www.corwinlattimore.example
    </address>
  </section>

  <section class="sheet card card-front" aria-label="Business card front">
    <div class="write-lines"><span></span><span></span><span></span><span></span></div>
    <div class="wordmark">Corwin Lattimore</div>
    <address class="contact">
      <span class="person">[firstname] [surname]</span><br>
      [title]<br>
      1 Some Street, Sometown<br>
      Somewhereshire SW23 8SW<br>
      someone@corwinlattimore.example
    </address>
  </section>

  <section class="sheet card card-back" aria-label="Business card back">
    <div class="wordmark">Corwin Lattimore</div>
    <div class="web">www.corwinlattimore.example</div>
  </section>

</body>
</html>
```